Total Health and Wellness Infographic

Hello,
We need an infographic of the 16 factors for total health and wellness.  We are imagining a circle pie chart with all 16 categories, with each pie having a corresponding graphic in it.
We want it to be modern, beautiful, easy to understand (we welcome cartoon graphics)
The 16 points are:
a. Sleep
b. Exercise/Movement
c. Macronutrient Diet
d. Micronutrients
e. Health Habits (Tracking, Morning Routines, Mindfulness/Meditation)
f. CV Health
g. GI Health
h. Brain Health
i. Inflammation (Food allergies, etc)
j. Hormone Health
k. Stress
l. Immunity and Cancer Detection/ Prevention
m. Detoxification – heavy metals, pesticides, your environment
n. Longevity
o. Sexual Health
p. Aesthetics – Facial, Hair, Body
Attached are our brand standards for reference.
Let us know if you have any questions.
Thank you!

```html
<!DOCTYPE html>
<html lang="en">
<head>
<meta charset="utf-8">
<title>16 Factors of Total Health and Wellness</title>
<link rel="stylesheet" href="https://fonts.googleapis.com/css2?family=Roboto+Condensed:wght@400;700&display=swap">
<style>
  :root {
    --bg-light: #f3f5f7;
    --bg-mid: #dfe5ea;
    --figure-dark: #2d5a74;
    --figure-mid: #4f86a3;
    --figure-light: #8fb6c9;
    --column-bg: #ffffff;
    --rule-green: #9ccc5a;
    --ink-dark: #3b3b3b;
    --ink-mid: #5b5b5b;
    --ink-teal: #22a4c6;
    --ink-light: #a3a3a3;
  }
  * { box-sizing: border-box; margin: 0; padding: 0; }
  html, body { width: 800px; height: 1200px; overflow: hidden; }
  body {
    font-family: "Roboto Condensed", "Arial Narrow", sans-serif;
    background: linear-gradient(160deg, var(--bg-light) 0%, var(--bg-mid) 55%, var(--bg-light) 100%);
    position: relative;
  }
  .backdrop-facets {
    position: absolute; inset: 0 0 100px 0;
    background: linear-gradient(200deg, #e7ecf0 0%, #f6f8f9 40%, #dde4e9 100%);
  }
  .figure {
    position: absolute; top: 26px; width: 250px; height: 1074px;
    border-radius: 110px 110px 30px 30px;
    background: linear-gradient(180deg, var(--figure-dark) 0%, var(--figure-mid) 55%, var(--figure-light) 100%);
    opacity: .9;
  }
  .figure--left { left: 18px; }
  .figure--right { right: 18px; }
  .factor-list {
    position: absolute; left: 200px; top: 0; width: 400px;
    list-style: none; background: var(--column-bg);
    border-left: 2px solid var(--rule-green);
    border-right: 2px solid var(--rule-green);
  }
  .factor {
    height: 68px; display: flex; align-items: center; gap: 14px;
    padding: 0 16px; border-bottom: 2px solid var(--rule-green);
    font-weight: 700; font-size: 27px; text-transform: uppercase; letter-spacing: .3px;
    white-space: nowrap;
  }
  .factor__icon {
    flex: none; width: 40px; height: 40px; border-radius: 8px;
    background: currentColor; display: flex; align-items: center; justify-content: center;
  }
  .factor__icon svg { width: 26px; height: 26px; }
  .factor__note { font-size: 12px; font-weight: 400; line-height: 1.15; white-space: normal; letter-spacing: 0; }
  .tone-dark { color: var(--ink-dark); }
  .tone-mid { color: var(--ink-mid); }
  .tone-teal { color: var(--ink-teal); }
  .tone-light { color: var(--ink-light); }
  .footer-band {
    position: absolute; left: 0; right: 0; bottom: 0; height: 100px; background: #ffffff;
  }
  .brand-name {
    position: absolute; right: 40px; bottom: 38px;
    font-weight: 700; font-size: 24px; letter-spacing: 1px; color: var(--ink-teal);
  }
</style>
</head>
<body>
  <div class="backdrop-facets" role="img" aria-label="Soft faceted grey geometric background"></div>
  <div class="figure figure--left" role="img" aria-label="Blue silhouette of a standing human body, front view"></div>
  <div class="figure figure--right" role="img" aria-label="Blue silhouette of a standing human body, back view"></div>

  <ul class="factor-list">
    <li class="factor tone-dark"><span class="factor__icon" role="img" aria-label="Bed icon"><svg viewBox="0 0 26 26"><rect x="3" y="13" width="20" height="6" fill="#fff"/><rect x="3" y="9" width="6" height="4" fill="#fff"/><rect x="3" y="19" width="2" height="3" fill="#fff"/><rect x="21" y="19" width="2" height="3" fill="#fff"/></svg></span>Sleep</li>
    <li class="factor tone-mid"><span class="factor__icon" role="img" aria-label="Movement icon"><svg viewBox="0 0 26 26"><circle cx="15" cy="5" r="3" fill="#fff"/><path d="M14 9 L10 16 L6 22 M12 13 L18 17 L20 23 M11 11 L6 12" stroke="#fff" stroke-width="2.5" fill="none" stroke-linecap="round"/></svg></span>Exercise/Movement</li>
    <li class="factor tone-teal"><span class="factor__icon" role="img" aria-label="Plate icon"><svg viewBox="0 0 26 26"><circle cx="13" cy="13" r="9" fill="none" stroke="#fff" stroke-width="2.5"/><circle cx="13" cy="13" r="4" fill="#fff"/></svg></span>Macronutrient Diet</li>
    <li class="factor tone-light"><span class="factor__icon" role="img" aria-label="Capsule icon"><svg viewBox="0 0 26 26"><rect x="9" y="3" width="8" height="20" rx="4" fill="none" stroke="#fff" stroke-width="2.5"/><line x1="9" y1="13" x2="17" y2="13" stroke="#fff" stroke-width="2.5"/></svg></span>Micronutrients</li>
    <li class="factor tone-dark"><span class="factor__icon" role="img" aria-label="Check icon"><svg viewBox="0 0 26 26"><path d="M5 13 L11 19 L21 7" stroke="#fff" stroke-width="3" fill="none" stroke-linecap="round"/></svg></span>Health <span class="factor__note">(Tracking, morning routines,<br>mindfulness/meditation)</span></li>
    <li class="factor tone-mid"><span class="factor__icon" role="img" aria-label="Heart icon"><svg viewBox="0 0 26 26"><path d="M13 22 L4 13 A5 5 0 0 1 13 7 A5 5 0 0 1 22 13 Z" fill="#fff"/></svg></span>CV Health</li>
    <li class="factor tone-teal"><span class="factor__icon" role="img" aria-label="Digestive icon"><svg viewBox="0 0 26 26"><path d="M8 4 V10 Q8 14 13 14 Q19 14 19 19 Q19 23 13 23" stroke="#fff" stroke-width="3" fill="none" stroke-linecap="round"/></svg></span>GI Health</li>
    <li class="factor tone-light"><span class="factor__icon" role="img" aria-label="Brain icon"><svg viewBox="0 0 26 26"><ellipse cx="13" cy="13" rx="9" ry="7" fill="none" stroke="#fff" stroke-width="2.5"/><line x1="13" y1="6" x2="13" y2="20" stroke="#fff" stroke-width="2"/></svg></span>Brain Health</li>
    <li class="factor tone-dark"><span class="factor__icon" role="img" aria-label="No icon"><svg viewBox="0 0 26 26"><circle cx="13" cy="13" r="9" fill="none" stroke="#fff" stroke-width="2.5"/><line x1="7" y1="7" x2="19" y2="19" stroke="#fff" stroke-width="2.5"/></svg></span>Inflammation <span class="factor__note">(Food allergies, etc)</span></li>
    <li class="factor tone-mid"><span class="factor__icon" role="img" aria-label="Molecule icon"><svg viewBox="0 0 26 26"><circle cx="13" cy="13" r="3.5" fill="#fff"/><circle cx="5" cy="7" r="2.5" fill="#fff"/><circle cx="21" cy="7" r="2.5" fill="#fff"/><circle cx="13" cy="22" r="2.5" fill="#fff"/><path d="M5 7 L13 13 L21 7 M13 13 V22" stroke="#fff" stroke-width="2"/></svg></span>Hormone Health</li>
    <li class="factor tone-teal"><span class="factor__icon" role="img" aria-label="Lightning icon"><svg viewBox="0 0 26 26"><path d="M15 3 L7 15 H12 L10 23 L19 10 H14 Z" fill="#fff"/></svg></span>Stress</li>
    <li class="factor tone-light"><span class="factor__icon" role="img" aria-label="Shield icon"><svg viewBox="0 0 26 26"><path d="M13 3 L21 6 V13 Q21 20 13 23 Q5 20 5 13 V6 Z" fill="#fff"/></svg></span>Immunity <span class="factor__note">&amp; cancer detection/prevention</span></li>
    <li class="factor tone-dark"><span class="factor__icon" role="img" aria-label="Drop icon"><svg viewBox="0 0 26 26"><path d="M13 3 Q20 12 20 16 A7 7 0 0 1 6 16 Q6 12 13 3 Z" fill="#fff"/></svg></span>Detoxification <span class="factor__note">Heavy metals,<br>pesticides, your environment</span></li>
    <li class="factor tone-mid"><span class="factor__icon" role="img" aria-label="Hourglass icon"><svg viewBox="0 0 26 26"><path d="M7 4 H19 L13 13 L19 22 H7 L13 13 Z" fill="#fff"/></svg></span>Longevity</li>
    <li class="factor tone-teal"><span class="factor__icon" role="img" aria-label="Arrow icon"><svg viewBox="0 0 26 26"><circle cx="11" cy="15" r="6" fill="none" stroke="#fff" stroke-width="2.5"/><path d="M15 11 L21 5 M16 5 H21 V10" stroke="#fff" stroke-width="2.5" fill="none"/></svg></span>Sexual Health</li>
    <li class="factor tone-light"><span class="factor__icon" role="img" aria-label="Eye icon"><svg viewBox="0 0 26 26"><path d="M3 13 Q13 3 23 13 Q13 23 3 13 Z" fill="none" stroke="#fff" stroke-width="2.5"/><circle cx="13" cy="13" r="3" fill="#fff"/></svg></span>Aesthetics <span class="factor__note">Facial, hair, body</span></li>
  </ul>

  <footer class="footer-band">
    <span class="brand-name">VITALCORE</span>
  </footer>
</body>
</html>
```